Upscale business cards needed for family office

We would like professional business cards created for employees of our family office. Relatively simple and straightforward, but also with a unique element to set them apart. Probably stick with neutral and simple colors that mesh well with the colors in the logo. We need space for the traditional elements, including name, title, address, email/phone number.

Industry/Entity Type

Business

Contact Information for Business Card

Space for name, title, phone number, email, address

```html
<!DOCTYPE html>
<html lang="en">
<head>
<meta charset="utf-8">
<title>Brightmere Business Cards</title>
<link href="https://fonts.googleapis.com/css2?family=Arimo:wght@400;700&display=swap" rel="stylesheet">
<style>
  :root {
    --page: #ecebe8;
    --card: #ffffff;
    --card-shade: #ececec;
    --ink: #2b2b2b;
    --mark: #5f6a70;
    --accent: #2aa6d9;
    --band: #1ec3da;
    --band-deep: #17a7c2;
    --icon: #ffffff;
  }
  * { box-sizing: border-box; margin: 0; padding: 0; }
  html, body {
    width: 1200px; height: 902px; overflow: hidden;
    background: var(--page);
    font-family: "Arimo", Arial, sans-serif;
  }
  .sheet {
    position: relative; width: 1200px; height: 902px;
    display: flex; flex-direction: column; align-items: center; justify-content: center; gap: 56px;
  }
  .card {
    position: relative; width: 630px; height: 360px;
    background: var(--card);
    box-shadow: 0 6px 18px rgba(0,0,0,.18);
    overflow: hidden;
  }
  .brand {
    display: flex; align-items: center; gap: 14px;
    color: var(--mark); font-weight: 400;
  }
  .brand-square { width: 22px; height: 22px; background: var(--band); }
  .card-front { display: flex; align-items: center; justify-content: center; }
  .card-front .brand { font-size: 46px; }
  .card-back .info-panel {
    position: absolute; left: 0; top: 0; bottom: 0; width: 62%;
    background: var(--card-shade);
  }
  .card-back .brand {
    position: absolute; right: 34px; top: 150px; font-size: 32px;
  }
  .card-back .brand .brand-square { width: 16px; height: 16px; }
  .person { position: absolute; left: 34px; top: 118px; }
  .person-name { font-size: 27px; color: var(--ink); line-height: 1.1; }
  .person-title { font-size: 20px; color: var(--accent); line-height: 1.2; }
  .contact-list { position: absolute; left: 0; top: 190px; list-style: none; }
  .contact-row {
    height: 44px; margin-bottom: 9px;
    display: flex; align-items: center;
    background: var(--band); color: var(--ink); font-size: 18px;
  }
  .contact-row:nth-child(1) { width: 420px; }
  .contact-row:nth-child(2) { width: 450px; }
  .contact-row:nth-child(3) { width: 480px; }
  .contact-icon {
    width: 56px; height: 100%; margin-right: 14px;
    background: var(--band-deep);
    display: flex; align-items: center; justify-content: center;
  }
  .contact-icon svg { width: 22px; height: 22px; }
</style>
</head>
<body>
<main class="sheet">
  <section class="card card-front">
    <div class="brand"><span class="brand-square"></span>Brightmere</div>
  </section>

  <section class="card card-back">
    <div class="info-panel"></div>
    <div class="person">
      <p class="person-name">Owen Carver</p>
      <p class="person-title">Managing Director</p>
    </div>
    <ul class="contact-list">
      <li class="contact-row">
        <span class="contact-icon">
          <svg viewBox="0 0 24 24" fill="none" stroke="var(--icon)" stroke-width="2"><rect x="6" y="2" width="12" height="20" rx="2"/><line x1="10" y1="18" x2="14" y2="18"/></svg>
        </span>021-555-0147
      </li>
      <li class="contact-row">
        <span class="contact-icon">
          <svg viewBox="0 0 24 24" fill="none" stroke="var(--icon)" stroke-width="2"><rect x="2" y="5" width="20" height="14" rx="1"/><polyline points="2,6 12,13 22,6"/></svg>
        </span>owen@brightmere.com
      </li>
      <li class="contact-row">
        <span class="contact-icon">
          <svg viewBox="0 0 24 24" fill="none" stroke="var(--icon)" stroke-width="2"><polyline points="3,11 12,3 21,11"/><path d="M5 10v11h14V10"/><rect x="10" y="14" width="4" height="7"/></svg>
        </span>48 Linden Grove Rd
      </li>
    </ul>
    <div class="brand"><span class="brand-square"></span>Brightmere</div>
  </section>
</main>
</body>
</html>
```